Business Card Design

Harbor Refuse 342 is a waste collection business contracted to remove waste from city streets, parks and caravan parks.

Target Market(s)

CEO and Managing Directors

Industry/Entity Type

Business

Contact Information for Business Card

Harbor Refuse 342
Manager
Dale Pickett
0439516204
harborrefuse342@quillmail.com.au

Colors
33a6d7
ecf7fb

Requirements
Must have
• Must have eye catching design that stands out above others ( tender process can be very competitive ).
Nice to have
• A garbage truck on or in the logo somehow

```html
<!DOCTYPE html>
<html lang="en">
<head>
<meta charset="utf-8">
<title>Harbor Refuse 342 – Business Card</title>
<link href="https://fonts.googleapis.com/css2?family=Open+Sans:wght@400;600;700&display=swap" rel="stylesheet">
<style>
  :root {
    --backdrop: #1f4464;
    --card: #eceef1;
    --card-edge: #d3d7dc;
    --brand-blue: #1d93d6;
    --ink: #222629;
    --ink-soft: #3a3f44;
    --white: #ffffff;
    --art-tone: #c9ced4;
  }
  * { margin: 0; padding: 0; box-sizing: border-box; }
  html, body {
    width: 1200px; height: 830px; overflow: hidden;
    background: var(--backdrop);
    font-family: "Open Sans", Arial, sans-serif;
  }
  .canvas { position: relative; width: 1200px; height: 830px; }

  .card {
    position: absolute;
    background: var(--card);
    border-radius: 34px;
    box-shadow: 0 0 0 1px var(--card-edge);
    overflow: hidden;
  }

  /* Front */
  .card-front { left: 40px; top: 36px; width: 690px; height: 378px; }
  .brand-name {
    position: absolute; left: 100px; top: 40px; width: 300px;
    text-align: right;
    font-size: 44px; font-weight: 600; color: var(--ink);
    line-height: 1.12; letter-spacing: -0.5px;
  }
  .brand-art {
    position: absolute; left: 408px; top: 92px;
    width: 152px; height: 94px; background: var(--art-tone);
  }
  .contact-band {
    position: absolute; left: 0; top: 268px;
    width: 100%; height: 96px; background: var(--brand-blue);
    color: var(--white);
  }
  .contact-name {
    position: absolute; left: 96px; top: 22px;
    font-size: 27px; font-weight: 400; letter-spacing: 0.3px;
  }
  .contact-role {
    position: absolute; left: 106px; top: 56px;
    font-size: 18px; font-weight: 400; letter-spacing: 0.5px;
  }
  .contact-phone {
    position: absolute; left: 354px; top: 30px;
    font-size: 24px; font-weight: 400;
  }
  .contact-phone strong { font-weight: 700; margin-left: 6px; }

  /* Back */
  .card-back { left: 500px; top: 420px; width: 630px; height: 370px; }
  .services-title {
    position: absolute; left: 120px; top: 70px;
    font-size: 19px; font-weight: 700; color: var(--ink);
  }
  .services-list {
    position: absolute; left: 120px; top: 118px;
    list-style: none;
  }
  .services-list li {
    position: relative; padding-left: 46px;
    font-size: 17px; font-weight: 700; color: var(--ink-soft);
    line-height: 27px; letter-spacing: 0.2px;
    white-space: nowrap;
  }
  .services-list li::before {
    content: ""; position: absolute; left: 10px; top: 12px;
    width: 5px; height: 5px; border-radius: 50%; background: var(--ink);
  }
  .services-contact {
    position: absolute; left: 0; width: 100%; top: 302px;
    text-align: center; padding-left: 130px;
    font-size: 16px; color: var(--ink-soft); letter-spacing: 0.8px;
  }
</style>
</head>
<body>
<main class="canvas">
  <section class="card card-front">
    <div class="brand-name">Harbor Refuse<br>342</div>
    <div class="brand-art" role="img" aria-label="Illustration of a garbage truck"></div>
    <div class="contact-band">
      <div class="contact-name">DALE PICKETT</div>
      <div class="contact-role">MANAGER</div>
      <div class="contact-phone">CALL: <strong>0439516204</strong></div>
    </div>
  </section>

  <section class="card card-back">
    <h2 class="services-title">SERVICES:</h2>
    <ul class="services-list">
      <li>STREET &amp; PARK WASTE COLLECTION</li>
      <li>CARAVAN PARK BIN SERVICE</li>
      <li>GENERAL WASTE REMOVAL</li>
      <li>RECYCLING &amp; GREEN WASTE PICKUP</li>
      <li>SKIP HIRE</li>
      <li>DOMESTIC &amp; COMMERCIAL</li>
    </ul>
    <div class="services-contact">harborrefuse342@quillmail.com.au</div>
  </section>
</main>
</body>
</html>
```